Quillo Design Prize - $10,000 tablet app design contest, Event App Category

Quillo is a marketplace for Velo App Templates (similar to PageLoom templates). We want you to design an app template for sale in our marketplace which targets Event Apps (Velo Apps that are created around music festivals, tradeshows, conferences or other events).

It’s up to you to create pages or features for the App Template that you think are appropriate. Creativity will be rewarded! Here are some example pages or features that you could create:

• A welcome page
• Event details – when and where?
• A location map
• A contact details page
• An event calendar (what’s on when?)
• Social media integration
• Video or animations

Your design should be Vibrant, Engaging and Contemporary. If you have an Velo, download Quillo Viewer and download template examples in the download tab.

Your entry must include:
• A brief description of your template
• preview images of all pages of your template

Attached to this project are free templates to help you get started with your design. We have included:
1. A free portfolio template for designers/photographers
2. Icons and artwork to use in your template
3. Blank pages template
4. Form template
5. Video ad template

If you are selected as a finalist you will be required to submit an .oproject file containing:
• Your InDesign source files
• Preview images of your template
• All creative / stock assets used in the template (animations, video etc.)
• A text file with instructions on how to update the template
• A metadata .txt file containing template details and your information

How to enter:
1. Register at Marketplace and view the instructions under the welcome message https://marketplace.quillohub-example.com/welcome
2. Download Quillo Editor: https://support.quillohub-example.com/entries/58174096-quillo-editor
3. Use the free templates provided in this brief to create your designs and submit to Pencilyard

Reason: Due to the Christmas break we are extending the deadline of our competition. Thank you for time and effort - I will be providing feedback over the next couple of days! Best wishes, Loretta

Hi All,

I have received many screenshots with some great designs! I just wanted to clarify that you are designing Quillo app templates including Quillo features and not just page designs?

Read Tips for First Time Quilloers to guide you through the template creation process

Before you start designing templates for Quillo Marketplace

·       Read the Quality Standards

·       Read the Copyright Information 

·       Use the Template Quality Checklist to ensure your template follows our guidelines. 

What should my project file contain?

·       A folder containing your source files, e.g. InDesign. This must be named Source.

·       The Quillo content files. This must be named Bundle.

·       Instructions, explaining to a customer how to use your template.

Best wishes,

Loretta

Reason: We are extending the competition by 7 days to give you more time!

Reason: Hello - we have received 3 entries for this contest so we are extending the deadline by 7 days. Best wishes, Loretta :)

Target Market(s)

Entrepreneurs who wish to create Velo Apps by using our App design templates.

Industry/Entity Type

Events

Requirements
Must have
• You will need Quillo Editor to open the .oproject files attached to this brief. Get it here: https://support.quillohub-example.com/entries/58174096-quillo-editor
Should not have
• Low quality, fuzzy or blurry images
- Any stock images or content which you do not own the rights to
- Any material which could be considered inappropriate or offensive

```html
<!DOCTYPE html>
<html lang="en">
<head>
<meta charset="utf-8">
<title>Event App – Welcome</title>
<link href="https://fonts.googleapis.com/css2?family=Fjalla+One&family=Playball&family=Ubuntu:wght@400;500&display=swap" rel="stylesheet">
<style>
:root{
  --black:#000;
  --status-text:#d8d8d8;
  --yellow:#fdbd0e;
  --yellow-dark:#e5a700;
  --nav-text:#4a3300;
  --nav-divider:#c58f00;
  --text:#f2f2f2;
  --accent:#ffc21a;
  --rule:#2f6d80;
  --bar-light:#b9c4c4;
  --bar-dark:#6f7d7e;
}
*{margin:0;padding:0;box-sizing:border-box}
html,body{width:948px;height:1200px;overflow:hidden;background:var(--black)}
.screen{position:relative;width:948px;height:1200px;overflow:hidden;font-family:"Ubuntu",sans-serif;color:var(--text);
  background:
    radial-gradient(ellipse 520px 380px at 300px 80px,rgba(74,140,160,.75),transparent 70%),
    radial-gradient(ellipse 500px 420px at 760px 120px,rgba(40,90,105,.55),transparent 70%),
    radial-gradient(ellipse 600px 400px at 200px 900px,rgba(70,20,20,.45),transparent 70%),
    linear-gradient(#1d4654 0,#0d1d24 380px,#0a0c0e 800px,#120707 1130px);}
.status-bar{height:32px;background:var(--black);display:flex;align-items:center;justify-content:space-between;padding:0 6px;color:var(--status-text);font:500 19px "Ubuntu",sans-serif}
.status-left{display:flex;align-items:center;gap:8px}
.status-right{display:flex;align-items:center;gap:12px}
.nav{display:grid;grid-template-columns:139px 176px 193px 143px 135px 162px;height:60px;background:linear-gradient(var(--yellow),var(--yellow-dark))}
.nav a{display:flex;align-items:center;justify-content:center;font:19px "Fjalla One",sans-serif;color:var(--nav-text);text-decoration:none;border-left:1px solid var(--nav-divider)}
.nav a:first-child{border-left:0}
.page-title{position:absolute;left:29px;top:112px;font:58px "Playball",cursive;color:#fff}
.title-rule{position:absolute;left:29px;top:198px;width:891px;height:1px;background:linear-gradient(90deg,var(--rule),rgba(47,109,128,.3))}
.intro{position:absolute;left:29px;top:230px;width:572px;font-size:15.4px;line-height:23.6px;letter-spacing:.15px}
.intro p{margin-bottom:23.6px}
.drop-cap{font-size:40px;line-height:20px;vertical-align:-1px}
.organiser{position:absolute;left:634px;top:235px;width:252px;text-align:center}
.portrait{width:252px;height:240px;border:2px solid #fff;border-radius:8px;background:radial-gradient(circle at 50% 40%,#1f3a42,#0a1316 75%)}
.organiser h2{margin-top:13px;font:400 27px "Fjalla One",sans-serif;color:var(--accent)}
.company{margin-top:8px;font:500 14.5px "Ubuntu",sans-serif}
.company span{color:var(--accent)}
.contact-list{list-style:none;margin-top:18px;text-align:left;padding-left:10px}
.contact-list li{display:flex;align-items:center;gap:12px;font:500 14.5px "Ubuntu",sans-serif;margin-bottom:18px}
.footer-bar{position:absolute;left:0;bottom:0;width:948px;height:70px;background:linear-gradient(var(--bar-light),var(--bar-dark) 48%,#0b0b0b 49%,#000)}
.next-btn{position:absolute;right:30px;bottom:15px;width:38px;height:36px;border-radius:4px;background:linear-gradient(#ffc83a,#e08f00);border:1px solid #8a5700;display:flex;align-items:center;justify-content:center}
</style>
</head>
<body>
<div class="screen">
  <div class="status-bar">
    <div class="status-left">Velo
      <svg width="24" height="18" viewBox="0 0 24 18"><path d="M2 6a14 14 0 0 1 20 0M5.5 9.5a9 9 0 0 1 13 0M9 13a4 4 0 0 1 6 0" fill="none" stroke="#d8d8d8" stroke-width="2.4" stroke-linecap="round"/><circle cx="12" cy="16" r="1.6" fill="#d8d8d8"/></svg>
    </div>
    <div>4:20 PM</div>
    <div class="status-right">
      <svg width="16" height="16" viewBox="0 0 16 16"><circle cx="8" cy="8" r="7" fill="#d8d8d8"/><path d="M8 3.5V8h3" stroke="#000" stroke-width="1.6" fill="none"/></svg>
      <svg width="32" height="16" viewBox="0 0 32 16"><rect x="1" y="2" width="27" height="12" rx="1.5" fill="none" stroke="#d8d8d8" stroke-width="1.6"/><rect x="3.5" y="4.5" width="22" height="7" fill="#d8d8d8"/><rect x="29" y="5.5" width="2.5" height="5" fill="#d8d8d8"/></svg>
    </div>
  </div>

  <nav class="nav">
    <a href="#">Welcome</a>
    <a href="#">Event Details</a>
    <a href="#">Event Calendar</a>
    <a href="#">Location</a>
    <a href="#">Contact</a>
    <a href="#">Get In touch</a>
  </nav>

  <h1 class="page-title">Welcome</h1>
  <div class="title-rule"></div>

  <div class="intro">
    <p><span class="drop-cap">L</span>orem ipsum dolor sit amet, consectetur adipiscing elit. Aliquam erat lorem, suscipit mattis ultrices in, eleifend eu sem. Aliquam lobortis semper nunc ut dapibus. Suspendisse potenti. Proin sed iaculis sem. In nec enim mi. Maecenas augue magna, fermentum eget fermentum sagittis, sodales sed erat. Duis mollis arcu laoreet augue gravida sed aliquam mauris porta. Fusce elit arcu, luctus vitae pharetra ac, rutrum at urna. Curabitur adipiscing vulputate leo vitae placerat. Duis et accumsan quam. Suspendisse ligula ante, lobortis nec cursus vitae, bibendum vel tortor. Ut massa neque, pharetra et dictum a, condimentum sed ligula. Curabitur quam odio, elementum ut lacinia eu, congue ac augue. Nam mattis sodales sodales.</p>
    <p>In hac habitasse platea dictumst. Fusce sollicitudin, nulla eu tempor accumsan, risus tellus luctus mauris, at blandit sem ligula id odio. Nulla mollis vehicula massa non tempor. Integer a tortor sed lorem porttitor rhoncus. Fusce ultrices sodales quam, non dapibus felis pulvinar sed. Etiam suscipit ullamcorper est sed accumsan. Aenean a odio id nibh iaculis porttitor nec ac nibh. Aenean in dolor nec enim ultrices viverra.</p>
    <p>Mauris hendrerit mi ut purus vehicula viverra. Maecenas a dolor ut purus luctus dignissim. Nullam quis orci sed libero bibendum blandit. Quisque ac velit enim. Proin non mauris nunc. Proin purus metus, eleifend et imperdiet vel, tincidunt eu leo. Phasellus ullamcorper risus non mauris sollicitudin quis tristique ante molestie. Ut aliquam tincidunt ante, id consectetur odio vehicula id. Quisque et eros justo. Vestibulum egestas, metus et rhoncus pellentesque, augue magna ultricies turpis, ut tempus nunc nibh sit amet turpis. Nam adipiscing ligula a lectus cursus ac ullamcorper risus fermentum. Aenean tempor suscipit nunc vel dictum. Quisque purus tortor, congue non cursus id, viverra eu ligula. Etiam molestie nibh in erat volutpat ut laoreet nibh aliquam. Quisque commodo semper aliquet.</p>
  </div>

  <aside class="organiser">
    <div class="portrait" role="img" aria-label="Portrait of the event organiser"></div>
    <h2>Event Organiser</h2>
    <p class="company">Company: <span>Brightfold Studio</span></p>
    <ul class="contact-list">
      <li>
        <svg width="30" height="20" viewBox="0 0 30 20"><rect x="1" y="1" width="28" height="18" rx="2" fill="#ffc21a" stroke="#c98a00"/><path d="M2 2l13 10 13-10" fill="none" stroke="#b07600" stroke-width="1.5"/></svg>
        info@brightfold-example.com
      </li>
      <li>
        <svg width="32" height="32" viewBox="0 0 32 32"><circle cx="16" cy="16" r="15" fill="#3ea6e0"/><path d="M11 8c-2 1-3 3-2 6 1 4 5 9 9 10 3 1 5 0 6-2l-3-3-2 2c-2-1-5-4-6-6l2-2z" fill="#fff"/></svg>
        91 40000 12345
      </li>
    </ul>
  </aside>

  <footer class="footer-bar">
    <a class="next-btn" href="#" aria-label="Next page">
      <svg width="16" height="20" viewBox="0 0 16 20"><path d="M4 2l8 8-8 8" fill="none" stroke="#2a1a00" stroke-width="3"/></svg>
    </a>
  </footer>
</div>
</body>
</html>
```